Innovative cost reduction consultant needs to build a group of technical advisors

We need to share our message and compassion for developing cost reduction in the automotive industry. We create opportunities for immediate innovation, by developing cost reduction solutions across suppliers with related process. Attached is an existing Power Point, but it needs improvement. Most of all, a good compelling story, why experts should join us.

Target Market(s)

Automotive industry, supply chain management

Industry/Entity Type

Automotive

Font styles to use
Serif
Sans Serif

Requirements
Must have
• Better visual graphics. There are a few, but they are not as visually appearing as I would like. A graphic with data should have a better visual impact then the ones that I created. I would like to share the message, that I am providing a solution for the automotive industry. The goal is to reduce costs and improve supplier and OEM relationships. The objective is to do so by creating opportunities for immediate innovation, by developing cost reduction solutions across suppliers with related processes. This message may need a visual graphic, which is missing from the presentation.
Nice to have
• Challenge my story and presentation. Does this make sense to you, and what is your opinions of the subject. Or, a relevant news source to validate the story.
Should not have
• I have not decided on the name of the venture or logo. So, let's just use my name as the source or writer. Derek Whitcombe, Cost Reduction Specialist. Thanks,

```html
<!DOCTYPE html>
<html lang="en">
<head>
<meta charset="utf-8">
<title>Development – Conceptual Model</title>
<link href="https://fonts.googleapis.com/css2?family=PT+Sans:wght@400;700&display=swap" rel="stylesheet">
<style>
  :root {
    --header-blue: #0b4ea2;
    --header-blue-dark: #083f87;
    --footer-blue: #1a9be0;
    --stripe: #e4e5e7;
    --paper: #ffffff;
    --bone-grey: #a7a9ac;
    --bone-grey-dark: #6d6e71;
    --node-magenta: #c8176a;
    --node-magenta-deep: #7d0c40;
    --label-blue: #1f8ad2;
    --label-orange: #ea8430;
    --start-green: #8cc63f;
    --end-green: #2fae3b;
    --white: #ffffff;
  }
  html, body {
    margin: 0;
    padding: 0;
    overflow: hidden;
  }
  body {
    width: 1200px;
    height: 650px;
    font-family: "PT Sans", "Helvetica Neue", Arial, sans-serif;
  }
  .slide {
    position: relative;
    width: 1200px;
    height: 650px;
    overflow: hidden;
    background:
      linear-gradient(90deg, rgba(255,255,255,0) 0%, rgba(255,255,255,0) 55%, rgba(255,255,255,0.95) 100%),
      repeating-linear-gradient(180deg, var(--paper) 0px, var(--paper) 6px, var(--stripe) 6px, var(--stripe) 11px);
  }
  .slide-header {
    position: absolute;
    left: 0; top: 0;
    width: 1200px;
    height: 99px;
    background: linear-gradient(180deg, var(--header-blue) 0%, var(--header-blue-dark) 100%);
  }
  .slide-title {
    margin: 0;
    position: absolute;
    left: 80px;
    top: 44px;
    color: var(--white);
    font-size: 45px;
    font-weight: 700;
    line-height: 1;
    letter-spacing: -0.5px;
  }
  .slide-footer {
    position: absolute;
    left: 0; bottom: 0;
    width: 1200px;
    height: 28px;
    background: var(--footer-blue);
  }
  .fishbone {
    position: absolute;
    left: 0; top: 0;
    width: 1200px;
    height: 650px;
  }
  .bone { stroke: var(--bone-grey); stroke-width: 7; stroke-linecap: butt; fill: none; }
  .node-circle { stroke: var(--white); stroke-width: 2.5; }
  .node-label { fill: var(--white); font-size: 15px; text-anchor: middle; }
  .hub-small { fill: var(--white); font-size: 17px; font-weight: 700; text-anchor: middle; }
  .hub-large { fill: var(--white); font-size: 32px; font-weight: 700; text-anchor: middle; }
  .cue { font-size: 12.5px; }
  .cue-blue { fill: var(--label-blue); }
  .cue-orange { fill: var(--label-orange); }
  .cue-end { text-anchor: end; }
  .pointer-blue { stroke: var(--label-blue); stroke-width: 1.3; }
  .pointer-orange { stroke: var(--label-orange); stroke-width: 1.3; }
</style>
</head>
<body>
<main class="slide">
  <header class="slide-header">
    <h1 class="slide-title">Development</h1>
  </header>

  <svg class="fishbone" viewBox="0 0 942 510" preserveAspectRatio="none" xmlns="http://www.w3.org/2000/svg">
    <defs>
      <radialGradient id="node-fill" cx="40%" cy="35%" r="70%">
        <stop offset="0%" stop-color="#e0287f"/>
        <stop offset="60%" stop-color="var(--node-magenta)"/>
        <stop offset="100%" stop-color="var(--node-magenta-deep)"/>
      </radialGradient>
      <filter id="node-shadow" x="-30%" y="-30%" width="160%" height="160%">
        <feDropShadow dx="1" dy="2" stdDeviation="2" flood-color="#000" flood-opacity="0.35"/>
      </filter>
      <marker id="bone-tip" viewBox="0 0 12 12" refX="2" refY="6" markerWidth="3.4" markerHeight="3.4" orient="auto">
        <polygon points="0,0 12,6 0,12" fill="var(--bone-grey-dark)"/>
        <polygon points="0,0 12,6 0,6" fill="#c8c9cb"/>
      </marker>
      <marker id="tip-blue" viewBox="0 0 10 10" refX="9" refY="5" markerWidth="6" markerHeight="6" orient="auto">
        <polygon points="0,1.5 10,5 0,8.5" fill="var(--label-blue)"/>
      </marker>
      <marker id="tip-orange" viewBox="0 0 10 10" refX="9" refY="5" markerWidth="6" markerHeight="6" orient="auto">
        <polygon points="0,1.5 10,5 0,8.5" fill="var(--label-orange)"/>
      </marker>
    </defs>

    <!-- spine -->
    <line class="bone" x1="80" y1="286" x2="855" y2="286"/>
    <polygon class="start-arrow" points="55,250 90,286 55,322" fill="var(--start-green)"/>
    <polygon class="end-arrow" points="850,250 886,286 850,322" fill="var(--end-green)"/>

    <!-- ribs -->
    <g class="ribs">
      <line class="bone" x1="205" y1="286" x2="128" y2="198" marker-end="url(#bone-tip)"/>
      <line class="bone" x1="205" y1="286" x2="128" y2="374" marker-end="url(#bone-tip)"/>
      <line class="bone" x1="335" y1="286" x2="258" y2="198" marker-end="url(#bone-tip)"/>
      <line class="bone" x1="335" y1="286" x2="258" y2="374" marker-end="url(#bone-tip)"/>
      <line class="bone" x1="665" y1="286" x2="752" y2="198" marker-end="url(#bone-tip)"/>
      <line class="bone" x1="610" y1="286" x2="686" y2="374" marker-end="url(#bone-tip)"/>
      <line class="bone" x1="735" y1="286" x2="815" y2="374" marker-end="url(#bone-tip)"/>
    </g>

    <!-- cause nodes -->
    <g class="node" filter="url(#node-shadow)">
      <circle class="node-circle" cx="97" cy="150" r="47" fill="url(#node-fill)"/>
      <text class="node-label" x="97" y="146">Advisor</text>
      <text class="node-label" x="97" y="166">Group</text>
    </g>
    <g class="node" filter="url(#node-shadow)">
      <circle class="node-circle" cx="227" cy="150" r="47" fill="url(#node-fill)"/>
      <text class="node-label" x="227" y="146">Supplier</text>
      <text class="node-label" x="227" y="166">Dashboard</text>
    </g>
    <g class="node" filter="url(#node-shadow)">
      <circle class="node-circle" cx="97" cy="420" r="47" fill="url(#node-fill)"/>
      <text class="node-label" x="97" y="414">Best</text>
      <text class="node-label" x="97" y="434">practices</text>
    </g>
    <g class="node" filter="url(#node-shadow)">
      <circle class="node-circle" cx="227" cy="420" r="47" fill="url(#node-fill)"/>
      <text class="node-label" x="227" y="415">Supplier</text>
      <text class="node-label" x="227" y="435">Data</text>
    </g>
    <g class="node" filter="url(#node-shadow)">
      <circle class="node-circle" cx="778" cy="150" r="47" fill="url(#node-fill)"/>
      <text class="node-label" x="778" y="146">OEM Data</text>
      <text class="node-label" x="778" y="166">New Model</text>
    </g>
    <g class="node" filter="url(#node-shadow)">
      <circle class="node-circle" cx="716" cy="420" r="47" fill="url(#node-fill)"/>
      <text class="node-label" x="716" y="415" style="font-size:14px">Business</text>
      <text class="node-label" x="716" y="434" style="font-size:14px">Development</text>
    </g>
    <g class="node" filter="url(#node-shadow)">
      <circle class="node-circle" cx="848" cy="420" r="47" fill="url(#node-fill)"/>
      <text class="node-label" x="848" y="415" style="font-size:14px">Supply chain</text>
      <text class="node-label" x="848" y="434" style="font-size:14px">Added value</text>
    </g>

    <!-- hub -->
    <g class="hub" filter="url(#node-shadow)">
      <circle class="node-circle" cx="489" cy="285" r="62" fill="url(#node-fill)" stroke-width="3"/>
      <text class="hub-small" x="489" y="273">Conceptual</text>
      <text class="hub-large" x="489" y="305">Model</text>
    </g>

    <!-- cues left -->
    <g class="cues">
      <text class="cue cue-blue" x="47" y="216">Build group</text>
      <line class="pointer-blue" x1="47" y1="224" x2="122" y2="224" marker-end="url(#tip-blue)"/>
      <text class="cue cue-blue" x="168" y="216">Key Drivers</text>
      <line class="pointer-blue" x1="168" y1="224" x2="244" y2="224" marker-end="url(#tip-blue)"/>
      <text class="cue cue-orange cue-end" x="377" y="217">Beta sites</text>
      <line class="pointer-orange" x1="377" y1="224" x2="304" y2="224" marker-end="url(#tip-orange)"/>
      <text class="cue cue-orange cue-end" x="277" y="253">Agreement</text>
      <line class="pointer-orange" x1="277" y1="261" x2="203" y2="261" marker-end="url(#tip-orange)"/>
      <text class="cue cue-orange cue-end" x="413" y="253">Costs</text>
      <line class="pointer-orange" x1="413" y1="261" x2="338" y2="261" marker-end="url(#tip-orange)"/>
      <text class="cue cue-blue" x="47" y="362">Categories</text>
      <line class="pointer-blue" x1="47" y1="369" x2="122" y2="369" marker-end="url(#tip-blue)"/>
      <text class="cue cue-blue" x="166" y="362">Survey</text>
      <line class="pointer-blue" x1="166" y1="369" x2="243" y2="369" marker-end="url(#tip-blue)"/>
      <text class="cue cue-orange cue-end" x="353" y="362">Research</text>
      <line class="pointer-orange" x1="353" y1="369" x2="276" y2="369" marker-end="url(#tip-orange)"/>
    </g>

    <!-- cues right -->
    <g class="cues">
      <text class="cue cue-blue" x="637" y="216">Text</text>
      <line class="pointer-blue" x1="630" y1="224" x2="706" y2="224" marker-end="url(#tip-blue)"/>
      <text class="cue cue-orange cue-end" x="820" y="219">Text</text>
      <line class="pointer-orange" x1="820" y1="226" x2="745" y2="226" marker-end="url(#tip-orange)"/>
      <text class="cue cue-orange cue-end" x="787" y="254">Text</text>
      <line class="pointer-orange" x1="787" y1="261" x2="712" y2="261" marker-end="url(#tip-orange)"/>
      <text class="cue cue-blue" x="572" y="336">Text</text>
      <line class="pointer-blue" x1="572" y1="345" x2="650" y2="345" marker-end="url(#tip-blue)"/>
      <text class="cue cue-orange cue-end" x="757" y="336">Text</text>
      <line class="pointer-orange" x1="757" y1="345" x2="682" y2="345" marker-end="url(#tip-orange)"/>
      <text class="cue cue-orange cue-end" x="883" y="336">Text</text>
      <line class="pointer-orange" x1="883" y1="345" x2="808" y2="345" marker-end="url(#tip-orange)"/>
    </g>
  </svg>

  <footer class="slide-footer"></footer>
</main>
</body>
</html>
```